Yard Sign Design Needed

Yard sign needed for mowing & landscaping company. Would like to use the top logo with black background which is attached. Would like MOWING to be in large standout letters. The word "landscaping" can be smaller and more artistic or omitted. Will need room for phone number once design is approved. The phone number will need to stand out and look identical/similar to the word 'MOWING"

```html
<!DOCTYPE html>
<html lang="en">
<head>
<meta charset="utf-8">
<title>Brenholt Contractors – Mowing Yard Signs</title>
<link href="https://fonts.googleapis.com/css2?family=Montserrat:wght@700;800&family=Mr+Dafoe&display=swap" rel="stylesheet">
<style>
  :root {
    --backdrop: #ececec;
    --sign-black: #000000;
    --sign-white: #ffffff;
    --brand-green: #97aa12;
    --green-deep: #869a1b;
    --green-light: #b3d152;
    --grey-light: #efefef;
    --grey-mid: #a9a9a9;
    --grey-dark: #666666;
    --ink: #000000;
  }
  html, body {
    margin: 0;
    padding: 0;
    width: 1200px;
    height: 704px;
    overflow: hidden;
    background: var(--backdrop);
  }
  .sign-board {
    position: relative;
    width: 1200px;
    height: 704px;
  }
  .yard-sign {
    position: absolute;
    top: 47px;
    width: 547px;
    height: 607px;
    display: block;
  }
  .yard-sign--green { left: 36px; }
  .yard-sign--grey { left: 617px; }
  .brand-name {
    font-family: "Montserrat", sans-serif;
    font-weight: 700;
    fill: var(--sign-white);
  }
  .headline {
    font-family: "Montserrat", sans-serif;
    font-weight: 800;
    fill: var(--sign-white);
  }
  .tagline {
    font-family: "Mr Dafoe", cursive;
    fill: var(--sign-white);
  }
  .call-label {
    font-family: "Montserrat", sans-serif;
    font-weight: 700;
    fill: var(--brand-green);
  }
  .phone-number {
    font-family: "Montserrat", sans-serif;
    font-weight: 800;
    fill: var(--ink);
  }
</style>
</head>
<body>
<main class="sign-board">

  <svg class="yard-sign yard-sign--green" viewBox="0 0 1149 1275" role="img" aria-label="Mowing yard sign, green swoosh version">
    <defs>
      <linearGradient id="swoosh-green" x1="0" y1="0" x2="1" y2="0">
        <stop offset="0" stop-color="var(--green-deep)"/>
        <stop offset="1" stop-color="var(--green-light)"/>
      </linearGradient>
    </defs>
    <rect class="sign-field" width="1149" height="1275" fill="var(--sign-black)"/>

    <g class="brand-block">
      <rect class="brand-square" x="524" y="140" width="90" height="90" fill="var(--brand-green)"/>
      <text class="brand-name" x="569" y="330" font-size="62" text-anchor="middle" letter-spacing="3">BRENHOLT</text>
      <text class="brand-name" x="569" y="395" font-size="30" text-anchor="middle" letter-spacing="4">CONTRACTORS LLC</text>
    </g>

    <text class="headline" x="574" y="617" font-size="158" text-anchor="middle" letter-spacing="10">MOWING</text>
    <text class="tagline" x="572" y="712" font-size="112" text-anchor="middle">Landscaping</text>

    <path class="swoosh" d="M0,985 C330,700 820,640 1149,1122 L1149,1275 L0,1275 Z" fill="url(#swoosh-green)"/>
    <path class="contact-panel" d="M0,1097 C350,740 840,720 1149,1124 L1149,1275 L0,1275 Z" fill="var(--sign-white)"/>

    <text class="call-label" x="556" y="1042" font-size="78" text-anchor="middle" letter-spacing="1">CALL NOW:</text>
    <text class="phone-number" x="553" y="1167" font-size="118" text-anchor="middle" letter-spacing="1">(555) 014-7392</text>
  </svg>

  <svg class="yard-sign yard-sign--grey" viewBox="0 0 1149 1275" role="img" aria-label="Mowing yard sign, grey swoosh version">
    <defs>
      <linearGradient id="swoosh-grey" x1="0" y1="0" x2="1" y2="0">
        <stop offset="0" stop-color="var(--grey-light)"/>
        <stop offset="0.5" stop-color="var(--grey-mid)"/>
        <stop offset="1" stop-color="var(--grey-dark)"/>
      </linearGradient>
    </defs>
    <rect class="sign-field" width="1149" height="1275" fill="var(--sign-black)"/>

    <g class="brand-block">
      <rect class="brand-square" x="524" y="140" width="90" height="90" fill="var(--brand-green)"/>
      <text class="brand-name" x="569" y="330" font-size="62" text-anchor="middle" letter-spacing="3">BRENHOLT</text>
      <text class="brand-name" x="569" y="395" font-size="30" text-anchor="middle" letter-spacing="4">CONTRACTORS LLC</text>
    </g>

    <text class="headline" x="574" y="617" font-size="158" text-anchor="middle" letter-spacing="10">MOWING</text>
    <text class="tagline" x="572" y="712" font-size="112" text-anchor="middle">Landscaping</text>

    <path class="swoosh" d="M0,985 C330,700 820,640 1149,1122 L1149,1275 L0,1275 Z" fill="url(#swoosh-grey)"/>
    <path class="contact-panel" d="M0,1097 C350,740 840,720 1149,1124 L1149,1275 L0,1275 Z" fill="var(--sign-white)"/>

    <text class="call-label" x="556" y="1042" font-size="78" text-anchor="middle" letter-spacing="1">CALL NOW:</text>
    <text class="phone-number" x="553" y="1167" font-size="118" text-anchor="middle" letter-spacing="1">(555) 014-7392</text>
  </svg>

</main>
</body>
</html>
```